Design a PowerPoint template for a consultancy organisation

I am after a Powerpoint template including three pages a title slide (that should have a title and subtitle), A title and content slide and a section header slide. I expect the company name and/or logo to be prominent and the colors to work well with the logo colors. I have included a copy of the logo

```html
<!DOCTYPE html>
<html lang="en">
<head>
<meta charset="utf-8">
<title>Consultancy Presentation Template</title>
<link rel="stylesheet" href="https://fonts.googleapis.com/css2?family=Manrope:wght@600;700;800&family=Montserrat:wght@400;500;600;700&display=swap">
<style>
  :root {
    --canvas: #bcbabb;
    --purple: #6a0dad;
    --purple-soft: #8a3cc4;
    --green: #8dc63f;
    --green-bright: #7ed321;
    --green-pale: #dcebc4;
    --lavender: #e6d9f2;
    --white: #ffffff;
    --ink: #2f3e4e;
  }
  * { margin: 0; padding: 0; box-sizing: border-box; }
  html, body {
    width: 710px;
    height: 1200px;
    overflow: hidden;
    background: var(--canvas);
  }
  .sheet {
    position: relative;
    width: 710px;
    height: 1200px;
  }
  .slide {
    position: absolute;
    overflow: hidden;
    background: var(--purple);
    font-family: "Manrope", sans-serif;
    color: var(--white);
  }
  .slide--title   { left: 46px; top: 50px;  width: 622px; height: 350px; }
  .slide--content { left: 48px; top: 435px; width: 617px; height: 348px; }
  .slide--section { left: 48px; top: 818px; width: 618px; height: 347px; }

  .slide__arcs {
    position: absolute;
    inset: 0;
    width: 100%;
    height: 100%;
  }

  .brand-badge {
    position: absolute;
    background: var(--white);
    display: flex;
    align-items: center;
    justify-content: center;
    gap: 5px;
  }
  .brand-badge__mark {
    width: 9px;
    height: 9px;
    background: var(--purple);
  }
  .brand-badge__name {
    font-family: "Manrope", sans-serif;
    font-weight: 700;
    color: var(--green);
    white-space: nowrap;
  }
  .brand-badge--large { width: 87px; height: 48px; }
  .brand-badge--large .brand-badge__name { font-size: 13px; }
  .brand-badge--small { width: 64px; height: 39px; gap: 3px; }
  .brand-badge--small .brand-badge__mark { width: 6px; height: 6px; }
  .brand-badge--small .brand-badge__name { font-size: 9.5px; }

  .headline {
    position: absolute;
    left: 0;
    right: 0;
    text-align: center;
    font-weight: 800;
    letter-spacing: -1px;
    line-height: 1.3;
    padding-bottom: 4px;
    background: linear-gradient(90deg, var(--green) 0%, var(--green) 30%, var(--green-pale) 75%, #f3f6ea 100%);
    -webkit-background-clip: text;
    background-clip: text;
    color: transparent;
  }
  .slide--title .headline { top: 183px; font-size: 43px; }
  .slide--section .headline { top: 190px; font-size: 42px; }

  .subtitle {
    position: absolute;
    left: 0;
    right: 0;
    top: 240px;
    text-align: center;
    font-weight: 600;
    font-size: 21px;
  }

  .web-address {
    position: absolute;
    left: 0;
    right: 0;
    text-align: center;
    font-family: "Montserrat", sans-serif;
    font-weight: 500;
    font-size: 11px;
    letter-spacing: 0.2px;
  }
  .slide--title .web-address { top: 309px; }
  .slide--section .web-address { top: 307px; }

  .content-heading {
    position: absolute;
    left: 51px;
    top: 37px;
    font-family: "Montserrat", sans-serif;
    font-weight: 700;
    font-size: 21px;
    line-height: 1.3;
    padding-bottom: 3px;
    background: linear-gradient(90deg, var(--purple-soft) 0%, var(--purple-soft) 25%, var(--lavender) 75%, var(--white) 100%);
    -webkit-background-clip: text;
    background-clip: text;
    color: transparent;
  }
  .content-subheading {
    position: absolute;
    left: 50px;
    top: 68px;
    font-weight: 600;
    font-size: 15px;
    line-height: 1;
  }

  .process-caption {
    position: absolute;
    left: 313px;
    width: 100px;
    top: 156px;
    text-align: center;
    font-family: "Montserrat", sans-serif;
    font-size: 9.5px;
    white-space: nowrap;
  }
  .process-frame {
    position: absolute;
    left: 234px;
    top: 179px;
    width: 251px;
    height: 129px;
    border: 1.5px solid var(--white);
  }
  .step {
    position: absolute;
    height: 36px;
    display: flex;
    align-items: center;
    justify-content: center;
    text-align: center;
    font-family: "Montserrat", sans-serif;
    font-weight: 700;
    font-size: 9.5px;
    line-height: 0.95;
    border: 1.5px solid var(--green);
  }
  .step--outer { background: var(--white); color: var(--ink); top: 228px; }
  .step--inner {
    background: var(--purple);
    color: var(--green-bright);
    border: 2px solid var(--green-bright);
    width: 95px;
    height: 34px;
  }

  .step--input     { left: 34px;  width: 58px; }
  .step--receiving { left: 122px; width: 80px; }
  .step--shipping  { left: 517px; width: 69px; }
  .step--check-in  { left: 251px; top: 195px; }
  .step--storage   { left: 375px; top: 195px; }
  .step--prep      { left: 251px; top: 257px; }
  .step--picking   { left: 375px; top: 257px; }

  .process-arrows {
    position: absolute;
    inset: 0;
    width: 100%;
    height: 100%;
  }
</style>
</head>
<body>
<main class="sheet">

  <!-- Title slide -->
  <section class="slide slide--title" aria-label="Title slide">
    <svg class="slide__arcs" viewBox="0 0 1300 731" preserveAspectRatio="none" aria-hidden="true">
      <circle cx="202" cy="-66" r="429" fill="var(--white)"/>
      <circle cx="206" cy="-36" r="312" fill="var(--green)"/>
    </svg>
    <div class="brand-badge brand-badge--large" style="left:63px; top:33px;">
      <span class="brand-badge__mark"></span>
      <span class="brand-badge__name">Brightdesk</span>
    </div>
    <h1 class="headline">Marketing Strategy</h1>
    <p class="subtitle">Presentation Subtitle</p>
    <p class="web-address">www.mycompany.com</p>
  </section>

  <!-- Title and content slide -->
  <section class="slide slide--content" aria-label="Title and content slide">
    <svg class="slide__arcs" viewBox="0 0 1290 727" preserveAspectRatio="none" aria-hidden="true">
      <circle cx="202" cy="-66" r="429" fill="var(--white)"/>
      <circle cx="206" cy="-36" r="312" fill="var(--green)"/>
    </svg>
    <h2 class="content-heading">Warehousing</h2>
    <p class="content-subheading">Process</p>
    <div class="brand-badge brand-badge--small" style="left:518px; top:25px;">
      <span class="brand-badge__mark"></span>
      <span class="brand-badge__name">Brightdesk</span>
    </div>

    <p class="process-caption">Warehouse Process</p>
    <div class="process-frame"></div>

    <div class="step step--outer step--input">INPUT</div>
    <div class="step step--outer step--receiving">Recieving</div>
    <div class="step step--outer step--shipping">Shipping</div>
    <div class="step step--inner step--check-in">Check In</div>
    <div class="step step--inner step--storage">Storage</div>
    <div class="step step--inner step--prep">Shipping<br>preparation</div>
    <div class="step step--inner step--picking">Order Picking</div>

    <svg class="process-arrows" viewBox="0 0 617 348" aria-hidden="true" fill="var(--white)">
      <g transform="translate(108 245)">
        <circle cx="-5" cy="0" r="1"/><path d="M-2 -4 L5 0 L-2 4 L0 0 Z"/>
      </g>
      <g transform="translate(218 245)">
        <circle cx="-5" cy="0" r="1"/><path d="M-2 -4 L5 0 L-2 4 L0 0 Z"/>
      </g>
      <g transform="translate(501 245)">
        <circle cx="-5" cy="0" r="1"/><path d="M-2 -4 L5 0 L-2 4 L0 0 Z"/>
      </g>
      <g transform="translate(360 212)">
        <circle cx="-5" cy="0" r="1"/><path d="M-2 -4 L5 0 L-2 4 L0 0 Z"/>
      </g>
      <g transform="translate(421 244) rotate(90)">
        <circle cx="-5" cy="0" r="1"/><path d="M-2 -4 L5 0 L-2 4 L0 0 Z"/>
      </g>
      <g transform="translate(360 275) rotate(180)">
        <circle cx="-5" cy="0" r="1"/><path d="M-2 -4 L5 0 L-2 4 L0 0 Z"/>
      </g>
    </svg>
  </section>

  <!-- Section header slide -->
  <section class="slide slide--section" aria-label="Section header slide">
    <svg class="slide__arcs" viewBox="0 0 1292 727" preserveAspectRatio="none" aria-hidden="true">
      <circle cx="202" cy="-66" r="429" fill="var(--white)"/>
      <circle cx="206" cy="-36" r="312" fill="var(--green)"/>
    </svg>
    <div class="brand-badge brand-badge--large" style="left:62px; top:33px;">
      <span class="brand-badge__mark"></span>
      <span class="brand-badge__name">Brightdesk</span>
    </div>
    <h2 class="headline">Section Title</h2>
    <p class="web-address">www.mycompany.com</p>
  </section>

</main>
</body>
</html>
```